Roofing & Siding door hanger flyer

-Looking to make door hanger flyer for Korvell Roofing & Siding
-4.5" wide x 11" tall
-2 sided full colour
-We have started a new website (the content is changing) I have attached photos.
-About us:
-25 year labour warranty's available
-32 years in Calgary
-QHT A+ Member
-NWPC (Prairie Westmark Shingle Council) (logo attached)
-TEK Summit Premier (logo attached)
-Owen Calloway (logo attached)
-Slogan "Raised On Grit, Proven Through Storms" 32 years in Calgary
-Sale
-Page 1 & 2 design ideas
We are in your area, contact us today for your Exclusive limited time offer! *discounts apply exclusively to new agreements only
Updates
-Please keep simple, clean & bright
-I really like the bright blue from our new logo (new logo uploaded)
-We specialize in Roofing -Siding-Gutters & full Exterior Renos (like the competitor example uploaded)
-This is the NEW website we are currently working on (not finished) https://mockups.plenvio.net/view/8b2c4e71-d95a-4f0b-b7e3-c1c1c8823a7f-9d2b/?fullscreen
-This is our OLD website https://northpeakshinglepros.com
-For the sale "We are in your area, contact us today for your Exclusive limited time offer" *discounts apply exclusively to new agreements only
-Free Estimates
-our phone# is 403-555-0187
-our website is northpeakshinglepros.com
-keep simple, clean, bright use the "new logo" uploaded. Check out the competitor example uploaded file
-We are in your area, Contact us today for your Exclusive limited time offer! *discounts apply to new agreements only
-FREE ESTIMATES
-Specialized in Roofing /Siding /Gutters Full Exterior Reno's
-We are currently working on a NEW website https://mockups.plenvio.net/view/8b2c4e71-d95a-4f0b-b7e3-c1c1c8823a7f-9d2b/?fullscreen
-Our OLD website https://northpeakshinglepros.com/
-Post old site address on flyer northpeakshinglepros.com
-Phone # 403-555-0187
Target Market(s)
40-55
Industry/Entity Type
Roofing Siding & full Exterior Reno's
Look and feel

```html
<!DOCTYPE html>
<html lang="en">
<head>
<meta charset="utf-8">
<title>Korvell Roofing &amp; Siding Door Hanger</title>
<link href="https://fonts.googleapis.com/css2?family=Montserrat:ital,wght@0,400;0,500;0,600;0,700;0,800;1,600;1,700;1,800&display=swap" rel="stylesheet">
<style>
:root{
  --stage:#cfcfd0;
  --panel:#f2f2f4;
  --blue:#1d63b0;
  --blue-bright:#3a8ee0;
  --blue-deep:#1a56a3;
  --ink:#1c1c1c;
  --grey-text:#555;
  --white:#fff;
  --gold:#d4a531;
}
*{box-sizing:border-box;margin:0;padding:0}
html,body{width:1019px;height:1200px;overflow:hidden;background:var(--stage)}
body{position:relative;font-family:'Montserrat',sans-serif;color:var(--ink)}
.hanger{position:absolute;top:100px;width:409px;height:999px;background:var(--panel);box-shadow:4px 6px 10px rgba(0,0,0,.25);overflow:hidden}
.hanger--front{left:78px}
.hanger--back{left:531px;background:var(--white)}
.hanger svg.art{position:absolute;left:0;top:0;width:409px;height:999px}
.t{position:absolute;left:0;width:100%;text-align:center;white-space:nowrap}
.neighbourhood{top:17px;font-size:18.5px;font-style:italic;font-weight:600;color:var(--grey-text);letter-spacing:.3px}
.hanger--back .neighbourhood{top:19px;color:var(--ink)}
.brand-name{top:270px;font-size:60px;font-weight:500;letter-spacing:3px;color:var(--ink);line-height:1}
.brand-sub{top:356px;font-size:24px;font-weight:500;letter-spacing:4px;color:var(--ink)}
.best{top:702px;font-size:34px;font-weight:400;color:#4a4a4a;line-height:1}
.experts{top:752px;font-size:46px;font-weight:800;color:var(--blue);line-height:40px}
.estimate-band{position:absolute;left:0;top:904px;width:409px;height:95px;background:linear-gradient(90deg,#1c58a6,#2d7cc9)}
.estimate-band .cta{top:12px;font-size:29px;font-weight:600;color:var(--white);letter-spacing:.3px}
.estimate-band .phone{top:44px;font-size:38px;font-weight:800;color:#111;display:flex;justify-content:center;align-items:center;gap:8px}
.phone-icon{width:36px;height:36px;border-radius:50%;background:#111;display:inline-flex;align-items:center;justify-content:center}
.label{position:absolute;font-size:11px;color:#444;letter-spacing:1.5px;transform:rotate(-90deg);transform-origin:left top}
.headline{top:244px;font-size:29px;font-weight:800;font-style:italic;color:var(--white);line-height:38px}
.years{top:326px;font-size:19px;font-weight:600;color:var(--blue-bright);letter-spacing:.8px}
.service{position:absolute;font-size:13px;font-weight:700;color:var(--white);letter-spacing:1px;white-space:nowrap}
.about{top:656px;font-size:11.5px;line-height:15.2px;color:#222}
.offer{top:755px;font-size:15px;font-weight:600;color:#2a7bd0;line-height:18px}
.fine{top:796px;font-size:10.5px;color:#222}
.contact-band{position:absolute;left:0;top:892px;width:409px;height:107px;background:linear-gradient(90deg,#1c58a6,#2f7fcc)}
.contact-tab{position:absolute;left:22px;top:2px;height:23px;padding:0 12px;background:#111;border-radius:6px 6px 0 0;color:var(--white);font-size:10.5px;font-weight:700;line-height:23px}
.contact-tab span{color:var(--blue-bright)}
.contact-list{position:absolute;left:28px;top:32px;list-style:none;color:var(--white);font-size:11.5px;line-height:15px}
.contact-list li{display:flex;gap:7px;margin-bottom:1px}
.contact-list svg{flex:none;margin-top:2px}
.contact-list .gap{margin-top:1px}
.back-brand{position:absolute;right:18px;top:28px;text-align:center;color:var(--white);font-weight:500}
.back-brand .n{font-size:34px;letter-spacing:2px;line-height:1}
.back-brand .s{font-size:11.5px;letter-spacing:2.4px;margin-top:8px}
</style>
</head>
<body>

<section class="hanger hanger--front">
  <svg class="art" viewBox="0 0 409 999">
    <defs>
      <linearGradient id="houseTone" x1="0" y1="0" x2="0" y2="1">
        <stop offset="0" stop-color="#cbb8d0"/>
        <stop offset=".3" stop-color="#53618e"/>
        <stop offset=".75" stop-color="#3b4766"/>
        <stop offset="1" stop-color="#6d7480"/>
      </linearGradient>
    </defs>
    <path d="M0,79 Q90,100 150,108 L150,137 Q80,140 0,168 Z" fill="var(--stage)"/>
    <circle cx="206" cy="123" r="62" fill="var(--stage)"/>
    <rect x="0" y="410" width="409" height="335" fill="url(#houseTone)" role="img" aria-label="Photo of a two-storey home with lit windows and garage at dusk"/>
    <polygon points="0,400 206,336 409,400 409,470 206,410 0,470" fill="var(--panel)"/>
    <polygon points="0,468 206,400 409,468 409,476 206,414 0,476" fill="var(--blue)"/>
    <polygon points="0,730 206,652 409,730 409,740 206,664 0,740" fill="var(--blue)"/>
    <polygon points="0,740 206,664 409,740 409,999 0,999" fill="var(--panel)"/>
    <circle cx="327" cy="690" r="47" fill="var(--gold)" role="img" aria-label="Labour warranty seal"/>
  </svg>
  <p class="t neighbourhood">WE ARE IN YOUR NEIGHBOURHOOD</p>
  <p class="t brand-name">KORVELL</p>
  <p class="t brand-sub">ROOFING &amp; SIDING</p>
  <p class="t best">BEST</p>
  <p class="t experts">ROOFING &amp;<br>SIDING<br>EXPERTS</p>
  <div class="estimate-band">
    <p class="t cta">GET A FREE ESTIMATE</p>
    <p class="t phone"><span class="phone-icon"><svg width="20" height="20" viewBox="0 0 24 24"><path d="M6.6 10.8c1.4 2.8 3.8 5.1 6.6 6.6l2.2-2.2c.3-.3.7-.4 1-.2 1.1.4 2.3.6 3.6.6.6 0 1 .4 1 1V20c0 .6-.4 1-1 1C10.6 21 3 13.4 3 4c0-.6.4-1 1-1h3.5c.6 0 1 .4 1 1 0 1.3.2 2.5.6 3.6.1.3 0 .7-.2 1z" fill="#fff"/></svg></span>(403)-555-0187</p>
  </div>
</section>

<section class="hanger hanger--back">
  <svg class="art" viewBox="0 0 409 999">
    <defs>
      <linearGradient id="roofTone" x1="0" y1="0" x2="0" y2="1">
        <stop offset="0" stop-color="#7d93b3"/>
        <stop offset=".25" stop-color="#3a3d46"/>
        <stop offset=".6" stop-color="#4a3526"/>
        <stop offset="1" stop-color="#000"/>
      </linearGradient>
      <linearGradient id="dormerTone" x1="0" y1="0" x2="1" y2="1"><stop offset="0" stop-color="#9fb8d6"/><stop offset=".5" stop-color="#2d3136"/><stop offset="1" stop-color="#3f4a36"/></linearGradient>
      <linearGradient id="sidingTone" x1="0" y1="0" x2="1" y2="1"><stop offset="0" stop-color="#6ea3d8"/><stop offset=".6" stop-color="#c9b79a"/><stop offset="1" stop-color="#56606b"/></linearGradient>
      <linearGradient id="gutterTone" x1="0" y1="0" x2="1" y2="1"><stop offset="0" stop-color="#b9c6d2"/><stop offset="1" stop-color="#f3f5f7"/></linearGradient>
      <linearGradient id="inspectTone" x1="0" y1="0" x2="1" y2="1"><stop offset="0" stop-color="#e6e4df"/><stop offset="1" stop-color="#c2c9cf"/></linearGradient>
    </defs>
    <rect x="0" y="0" width="409" height="345" fill="url(#roofTone)" role="img" aria-label="Photo of two workers installing a dark metal roof"/>
    <path d="M409,77 Q320,100 260,108 L260,137 Q330,140 409,164 Z" fill="var(--stage)"/>
    <circle cx="206" cy="123" r="62" fill="var(--stage)"/>
    <polygon points="0,336 206,384 409,336 409,346 206,396 0,346" fill="var(--blue-bright)"/>
    <polygon points="0,310 409,310 409,336 206,384 0,336" fill="#000"/>
    <polygon points="0,346 206,396 206,518 0,470" fill="url(#dormerTone)" role="img" aria-label="Photo of a shingled roof with dormers"/>
    <polygon points="206,396 409,346 409,462 206,518" fill="url(#sidingTone)" role="img" aria-label="Photo of a house gable with new siding"/>
    <polygon points="0,470 206,518 206,644 0,563" fill="url(#gutterTone)" role="img" aria-label="Photo of white gutters and downspout"/>
    <polygon points="206,518 409,462 409,570 206,644" fill="url(#inspectTone)" role="img" aria-label="Photo of a worker inspecting a soffit"/>
    <polygon points="0,452 206,500 206,518 0,470" fill="#111"/>
    <polygon points="206,500 409,444 409,462 206,518" fill="#111"/>
    <polygon points="0,545 206,626 206,644 0,563" fill="#111"/>
    <polygon points="206,626 409,552 409,570 206,644" fill="#111"/>
    <polygon points="0,563 206,644 409,570 409,580 206,656 0,573" fill="var(--blue)"/>
    <rect x="204.5" y="392" width="3" height="258" fill="var(--blue)"/>
    <rect x="22" y="837" width="44" height="34" fill="#2a4f86" role="img" aria-label="NWPC member badge"/>
    <rect x="80" y="840" width="72" height="28" rx="4" fill="#1d5a9c" role="img" aria-label="QHT accredited badge"/>
    <rect x="167" y="836" width="30" height="36" fill="#d8202a" role="img" aria-label="Shingle supplier badge"/>
    <circle cx="227" cy="854" r="19" fill="var(--gold)" role="img" aria-label="32 years anniversary seal"/>
    <circle cx="292" cy="854" r="14" fill="#2e8b3a" role="img" aria-label="Owen Calloway partner badge"/>
    <polygon points="356,824 384,854 356,884 328,854" fill="#1e3b70" role="img" aria-label="TEK Summit Premier badge"/>
  </svg>
  <p class="t neighbourhood">WE ARE IN YOUR NEIGHBOURHOOD</p>
  <p class="t headline">Raised On Grit<br>Proven Through Storms</p>
  <p class="t years">32 YEARS IN CALGARY</p>
  <span class="service" style="left:103px;top:485px;transform:translate(-50%,-50%) rotate(13deg)">ROOFING</span>
  <span class="service" style="left:305px;top:481px;transform:translate(-50%,-50%) rotate(-15deg)">SIDING</span>
  <span class="service" style="left:103px;top:594px;transform:translate(-50%,-50%) rotate(21.5deg)">GUTTERS &amp; METALS</span>
  <span class="service" style="left:307px;top:598px;transform:translate(-50%,-50%) rotate(-20deg)">INSPECTIONS</span>
  <p class="t about">We pride ourselves in providing excellent customer<br>service and quality workmanship.<br>We work with honesty and integrity and staff expert<br>managers, supervisors and trades people. We provide<br>satisfaction and ease of mind through our knowledge<br>and experience throughout the duration of the project.</p>
  <p class="t offer">We are in your area, contact us today<br>for your Exclusive limited time offer!</p>
  <p class="t fine">*discounts apply exclusively to new agreements only</p>
  <div class="contact-band">
    <div class="contact-tab">GET IN TOUCH <span>WITH US</span></div>
    <ul class="contact-list">
      <li><svg width="11" height="11" viewBox="0 0 24 24"><path d="M12 2a7 7 0 0 0-7 7c0 5 7 13 7 13s7-8 7-13a7 7 0 0 0-7-7zm0 9.5A2.5 2.5 0 1 1 12 6.5a2.5 2.5 0 0 1 0 5z" fill="#111"/></svg><span>4820 - 9 Street S.E. Calgary,<br>Alberta T2H 0K4</span></li>
      <li class="gap"><svg width="11" height="11" viewBox="0 0 24 24"><circle cx="12" cy="12" r="11" fill="#111"/><rect x="6" y="8" width="12" height="8" fill="#fff"/></svg><span>korvellroof@mailhub.net</span></li>
      <li><svg width="11" height="11" viewBox="0 0 24 24"><circle cx="12" cy="12" r="11" fill="#111"/><circle cx="12" cy="12" r="6" fill="none" stroke="#fff" stroke-width="2"/><line x1="6" y1="12" x2="18" y2="12" stroke="#fff" stroke-width="2"/></svg><span>www.northpeakshinglepros.com</span></li>
    </ul>
    <div class="back-brand"><p class="n">KORVELL</p><p class="s">ROOFING &amp; SIDING</p></div>
  </div>
</section>

<p class="label" style="left:44px;top:1099px">FRONT</p>
<p class="label" style="left:957px;top:1097px">BACK</p>

</body>
</html>
```